Wine labels Mirador Wine Council - Nueva etiqueta El Consejo Regulador de vinos de Palomar

Mirador Wines Council, based in southern Spain, are looking to create a new suite of wine labels which retain the elegance of the Sherry Wines industry while reinvigorating their image to the modern era and a new generation of Sherry Wine lovers. These labels will be used across the Mirador Wines Council's range of wines for the promotion of the Sherry Wines industry.

Your design must present at least two styles of Sherry Wines which demonstrate an elegant, modern interpretation and understanding of the unique mood and personality for these wines and the essence of southern Spain.

10 labels will be created based on the winning design, one for each of the unique varieties of Sherry Wines within the collection. This collection comprises of several different wine varieties including: Fino, Manzanilla, Amontillado, Oloroso, Palo Cortado, Medium, Cream, Pale Cream, Pedro Ximenez and Moscatel.

We recommend you visit our website www.miradorvinos.example/wines as the source to understanding the origins and unique personality of these diverse wines.

El Consejo Regulador de los Vinos de Palomar y Albencia quiere renovar las etiquetas de los vinos utilizados para sus actividades de promoción genérica. Esta colección de vinos comprende las tipologías más importantes de la región que incluye: fino, manzanilla, amontillado, oloroso, palo cortado, pale cream, medium, cream, pedro ximénez y moscatel. Por lo tanto se precisan 10 etiquetas, una para cada uno de los vinos mencionados.
Updates

Project Deadline Extended
Reason: Due to some confusion with the deadline we wish to officially extend the deadline to allow designers one last week to submit their entries.

Target Market(s)

Industry, journalists, media, sommeliers, chefs, wine writers

Industry/Entity Type

Council

Requirements
Must have
• Front and Back label plus capsule:
• Front label can have either of the two official logos of the Mirador Wine council titled Vinos de Palomar Digital or not, this is optional. Must include: Vino selecionado por el Consejo Regulador de la Denominacion de Origen, Name of the variety of wine eg FINO, percentage of alcohol eg 15% and quantity 75 cl.
• The back of the label must include the council logo titled Precinta and 4 additional logos positioned smaller. The Europa logo must appear larger than the 3 other logos. Space for descriptive text about the wine is also required.
• The dimensions of the bottle can be found at this link http://www.vidrialta.example/es/catalogo/vinos-y-espumosos/bordelesas/bd-corvina
• Altura:305 mm
• Diámetro base:76,20 mm
• Diámetro hombro:82 mm
• Tipo boca:Cetie
• Peso:750 gr
• Capacidad:75 cl
• Etiqueta delantera y trasera y capsula
• La etiqueta delantera puede incluir el logo oficial del Consejo Regulador o el logo digital, o ninguno, esto es opcional. Debe incluir el siguiete texto: Vino selecionado por el Consejo Regulador de la Denominacion de Origen, el nombre de la variedad del vino, por ejemplo Fino, el porcentaje de alcohol, por ejemplo 15%, y la capacidad 75cl.
• La etiqueta trasera debe incluir el logo oficial Precinta del Consejo, y cuatro logos adicionales con una dimension menor. El Logo de ¨Campos Unidos por el Mañana¨ debe ser de mayor tamaño que los otros. Se precisa espacio para el texto descriptivo de los vinos.
• Las dimensiones de la botella se puede encontrar en este enlace
• http://www.vidrialta.example/es/catalogo/vinos-y-espumosos/bordelesas/bd-corvina
• Altura:305 mm
• Diámetro base:76,20 mm
• Diámetro hombro:82 mm
• Tipo boca:Cetie
• Peso:750 gr
• Capacidad:75 cl
Nice to have
• See our website miradorvinos.example to understand the origin of the wines. Ver nuestra página web miradorvinos.example para mejor entender los vinos.
Should not have
• Images of catavinos or stereotypical images from Spain such as flamenco dancers or guitars.

```html
<!DOCTYPE html>
<html lang="es">
<head>
<meta charset="utf-8">
<title>Fino – Etiqueta delantera</title>
<link rel="stylesheet" href="https://fonts.googleapis.com/css2?family=Playfair+Display:wght@900&family=Jost:wght@400&display=swap">
<style>
  :root {
    --paper: #ffffff;
    --ink: #111111;
    --ink-soft: #3a3a3a;
    --edge: #9a9a9a;
    --lime: #80ff00;
    --leaf: #22cc00;
    --sage: #d3e0a0;
  }
  html, body {
    margin: 0;
    padding: 0;
    overflow: hidden;
    background: var(--paper);
  }
  .label {
    position: relative;
    width: 672px;
    height: 1200px;
    background: var(--paper);
    border-left: 1px solid var(--edge);
    box-sizing: border-box;
    overflow: hidden;
  }
  .variety {
    position: absolute;
    top: 140px;
    left: 0;
    width: 672px;
    margin: 0;
    text-align: center;
    font-family: "Playfair Display", serif;
    font-weight: 900;
    font-size: 101px;
    line-height: 1;
    letter-spacing: 2px;
    color: var(--ink);
    padding-left: 10px;
    box-sizing: border-box;
  }
  .designation {
    position: absolute;
    top: 258px;
    left: 77px;
    margin: 0;
    font-family: "Jost", sans-serif;
    font-weight: 400;
    font-size: 18.5px;
    line-height: 17.5px;
    letter-spacing: 0.6px;
    text-transform: uppercase;
    color: var(--ink-soft);
  }
  .specs {
    position: absolute;
    top: 298px;
    left: 436px;
    margin: 0;
    font-family: "Jost", sans-serif;
    font-weight: 400;
    font-size: 26px;
    line-height: 1;
    color: var(--ink-soft);
    white-space: nowrap;
  }
  .pattern-band {
    position: absolute;
    left: 0;
    top: 528px;
    width: 672px;
    height: 672px;
    display: block;
  }
</style>
</head>
<body>
  <main class="label">
    <h1 class="variety">Fino</h1>
    <p class="designation">Vino selecionado por el<br>consejo regulador de la<br>denominacion de origen</p>
    <p class="specs">75cl 15%alc.</p>
    <svg class="pattern-band" viewBox="0 0 672 672" role="img" aria-label="Patrón decorativo de franjas en zigzag verde lima, verde hoja y salvia sobre blanco">
      <defs>
        <linearGradient id="band-tones" x1="0" y1="0" x2="1" y2="1">
          <stop offset="0" stop-color="var(--lime)"/>
          <stop offset="0.55" stop-color="#9bf02a"/>
          <stop offset="1" stop-color="var(--lime)"/>
        </linearGradient>
      </defs>
      <rect x="0" y="0" width="672" height="672" fill="url(#band-tones)"/>
    </svg>
  </main>
</body>
</html>
```